New Human Resources Outsourcing company needs a brochure to explain services

I need a brochure that describes my business and the services we offer.

Everything we do is on my website as well. www.kelvorastaffing.com

Target Market(s)

Business Owners (Manufacturing, I.T. Financial Services)

Industry/Entity Type

Business

```html
<!DOCTYPE html>
<html lang="en">
<head>
<meta charset="utf-8">
<title>Kelvora Staffing – HR Solutions Brochure</title>
<link href="https://fonts.googleapis.com/css2?family=Lato:wght@400;700;900&family=Arimo:wght@400;700&family=Cinzel:wght@400;600&display=swap" rel="stylesheet">
<style>
  :root{
    --purple:#6b2a93;
    --purple-bright:#8a33b8;
    --purple-deep:#5a2180;
    --teal:#22d3c8;
    --paper:#f4f4f4;
    --ink:#333333;
    --ink-soft:#444444;
    --white:#ffffff;
    --backdrop:#e6e6e6;
  }
  *{box-sizing:border-box;margin:0;padding:0}
  html,body{width:806px;height:1200px;overflow:hidden;background:var(--backdrop)}
  body{font-family:'Lato',sans-serif;color:var(--ink)}
  .canvas{position:relative;width:806px;height:1200px;overflow:hidden}
  .brochure{position:absolute;left:45px;width:669px;height:477px;transform:scale(1.0718);transform-origin:0 0;box-shadow:0 3px 8px rgba(0,0,0,.25);overflow:hidden}
  .brochure--outside{top:62px}
  .brochure--inside{top:627px}
  .brochure > svg.shapes{position:absolute;left:0;top:0}
  .photo{position:absolute}
  .abs{position:absolute}

  .headline{left:12px;top:14px;color:var(--white);font-weight:900;line-height:1}
  .headline .lead{display:block;font-size:14px;letter-spacing:.2px}
  .headline .main{display:block;font-size:17px;font-weight:400;margin-top:3px;letter-spacing:.3px}

  .body-copy{font-size:8.6px;line-height:10.6px;color:var(--ink-soft);text-align:justify}

  .tag{position:absolute;height:18px;padding:0 20px 0 12px;color:var(--white);font-weight:900;font-size:10px;line-height:18px;background:var(--purple);clip-path:polygon(0 0,100% 0,calc(100% - 6px) 100%,0 100%)}
  .tag--light{background:var(--white);color:var(--purple-deep)}

  .checklist{list-style:none;font-size:8.8px;font-weight:700;color:var(--ink)}
  .checklist li{position:relative;padding-left:12px;height:18.7px;line-height:18.7px}
  .checklist li::before{content:"";position:absolute;left:1px;top:6px;width:3px;height:6px;border-right:1.6px solid var(--purple);border-bottom:1.6px solid var(--purple);transform:rotate(40deg)}
  .checklist li.plain::before{display:none}
  .checklist--light{color:var(--white)}
  .checklist--light li::before{border-color:var(--teal)}

  .contact{left:225px;width:219px;top:272px;text-align:center;color:var(--white);font-weight:700;font-size:11px;line-height:19px}
  .contact svg{vertical-align:-1px;margin-right:3px}

  .brand{left:502px;top:18px;display:flex;align-items:center;gap:6px;font-family:'Cinzel',serif;color:var(--purple);font-size:13px;font-weight:600;letter-spacing:.5px}
  .brand .mark{width:22px;height:22px;background:var(--purple)}

  .title-serif{left:444px;width:225px;top:282px;text-align:center;font-family:'Cinzel',serif;color:var(--purple);font-size:21px;letter-spacing:1px}
  .subtitle{left:444px;width:225px;top:310px;text-align:center;font-family:'Arimo',sans-serif;font-size:11.5px;color:var(--ink);letter-spacing:.2px}
  .call{left:444px;width:225px;top:382px;text-align:center;font-family:'Arimo',sans-serif;font-weight:700;font-size:15px;color:var(--white)}
  .call span{color:var(--teal)}
  .web{left:444px;width:225px;top:443px;text-align:center;font-family:'Arimo',sans-serif;font-weight:700;font-size:10px;letter-spacing:2.2px;color:var(--ink)}

  .pitch-title{left:240px;top:376px;color:var(--teal);font-family:'Arimo',sans-serif;font-weight:700;font-size:17px;line-height:1}
  .pitch-sub{left:240px;top:396px;color:var(--white);font-weight:700;font-size:10px}
  .pitch-rule{left:240px;top:411px;width:196px;height:1px;background:var(--white)}
  .pitch-copy{left:240px;top:416px;width:196px;color:var(--white);font-size:8.6px;line-height:10.6px;text-align:justify}

  .experience-a{left:463px;top:197px;color:var(--purple);font-family:'Arimo',sans-serif;font-weight:700;font-size:18px}
  .experience-b{left:463px;top:219px;color:var(--ink);font-family:'Arimo',sans-serif;font-size:25px}
  .experience-copy{left:463px;top:264px;width:195px}

  .benefits{list-style:none;left:463px;top:379px;font-size:8.8px;font-weight:700;color:var(--ink)}
  .benefits li{display:flex;align-items:center;gap:8px;height:22.6px}
  .benefits .dot{width:17px;height:17px;border-radius:50%;background:var(--purple);display:flex;align-items:center;justify-content:center}
</style>
</head>
<body>
<div class="canvas">

  <!-- Outside spread -->
  <section class="brochure brochure--outside">
    <svg class="shapes" width="669" height="477" viewBox="0 0 669 477" aria-hidden="true">
      <rect x="0" y="0" width="225" height="477" fill="var(--paper)"/>
      <polygon points="0,0 225,0 225,50 0,92" fill="var(--purple)"/>
      <polygon points="0,97 225,56 225,63 0,104" fill="var(--teal)"/>
      <polygon points="0,477 225,477 225,440 0,462" fill="var(--purple)"/>
      <rect x="225" y="0" width="219" height="477" fill="var(--teal)"/>
      <polygon points="225,0 444,0 444,258 374,190 258,190 258,44 225,50" fill="var(--purple-bright)"/>
      <line x1="370" y1="186" x2="446" y2="262" stroke="var(--white)" stroke-width="6"/>
      <polygon points="225,477 444,477 444,430 225,455" fill="var(--purple-deep)"/>
      <rect x="444" y="0" width="225" height="477" fill="var(--paper)"/>
      <polygon points="444,76 669,56 669,63 444,83" fill="var(--teal)"/>
      <polygon points="444,86 669,66 669,72 444,92" fill="var(--purple)"/>
      <polygon points="444,262 669,240 669,248 444,270" fill="var(--purple)"/>
      <polygon points="444,364 669,344 669,432 444,432" fill="var(--purple)"/>
      <rect x="444" y="432" width="225" height="3" fill="var(--teal)"/>
      <rect x="258" y="37" width="152" height="150" fill="var(--white)"/>
    </svg>
    <svg class="photo" style="left:264px;top:43px" width="140" height="138" role="img" aria-label="Photo of two colleagues working together at a computer in an office">
      <defs><linearGradient id="g1" x1="0" y1="0" x2="1" y2="1"><stop offset="0" stop-color="#dfe3e6"/><stop offset="1" stop-color="#6e7378"/></linearGradient></defs>
      <rect width="140" height="138" fill="url(#g1)"/>
    </svg>
    <svg class="photo" style="left:444px;top:72px" width="225" height="190" role="img" aria-label="Photo of three smiling business people giving a thumbs up">
      <defs><linearGradient id="g2" x1="0" y1="0" x2="1" y2="1"><stop offset="0" stop-color="#e9ecef"/><stop offset="1" stop-color="#8a8f96"/></linearGradient></defs>
      <polygon points="0,20 225,0 225,168 0,190" fill="url(#g2)"/>
    </svg>

    <h1 class="abs headline"><span class="lead">SOLUTIONS FOR HR</span><span class="main">PROFESSIONALS</span></h1>
    <p class="abs body-copy" style="left:12px;top:114px;width:200px">You're an HR professional and you probably have a lot on your plate. That's exactly why you need a good partner to help you minimize the frustrations of getting the HR job done. As your strategic partner, Kelvora Staffing will help you look good! Sometimes day to day stuff can get pretty hectic, that is why you need a partner.</p>
    <div class="tag" style="left:0;top:218px">WE CAN ASSIST YOU WITH</div>
    <ul class="abs checklist" style="left:12px;top:251px">
      <li>Providing Administrative Assistance</li>
      <li>HR Compliance Assesments</li>
      <li>Performance Management</li>
      <li>Leadership Training</li>
      <li>Employee Handbooks</li>
      <li>Employee Investigations</li>
      <li>Onboarding and Separations</li>
      <li>Internal I-9 Audits</li>
      <li>Sexual Harassment Prevention Training</li>
      <li>Succession Planning</li>
    </ul>

    <address class="abs contact" style="font-style:normal">
      <div><svg width="9" height="9" viewBox="0 0 10 10"><path d="M2 1l2 2-1 1.5c.8 1.3 1.6 2.1 2.6 2.6L7 6l2 2-1.4 1.5C4.5 9 1 5.6.5 2.4z" fill="var(--purple)"/></svg>(555) 204-7716</div>
      <div>FAX: (555) 204-7717</div>
      <div><svg width="10" height="8" viewBox="0 0 10 8"><rect width="10" height="8" fill="var(--purple)"/><path d="M0 0l5 4 5-4" stroke="var(--white)" fill="none"/></svg>info@kelvorastaffing.com</div>
      <div><svg width="9" height="9" viewBox="0 0 10 10"><circle cx="5" cy="5" r="4.5" fill="var(--purple)"/></svg>www.kelvorastaffing.com</div>
      <div><svg width="8" height="10" viewBox="0 0 8 10"><path d="M4 0a4 4 0 014 4c0 3-4 6-4 6S0 7 0 4a4 4 0 014-4z" fill="var(--purple)"/><circle cx="4" cy="4" r="1.4" fill="var(--white)"/></svg>2280 Harbor Ridge,</div>
      <div>#310 Larkmont,</div>
    </address>

    <div class="abs brand"><span class="mark"></span>Kelvora Staffing</div>
    <h2 class="abs title-serif">HR SOLUTIONS</h2>
    <p class="abs subtitle">FOR THE BUSINESS OWNER</p>
    <p class="abs call"><span>Call us</span> (555) 204-7716</p>
    <p class="abs web">www.kelvorastaffing.com</p>
  </section>

  <!-- Inside spread -->
  <section class="brochure brochure--inside">
    <svg class="shapes" width="669" height="477" viewBox="0 0 669 477" aria-hidden="true">
      <rect x="0" y="0" width="225" height="477" fill="var(--paper)"/>
      <rect x="225" y="0" width="219" height="477" fill="var(--purple-bright)"/>
      <polygon points="225,232 444,188 444,195 225,239" fill="var(--teal)"/>
      <polygon points="225,362 444,336 444,342 225,368" fill="var(--teal)"/>
      <polygon points="225,368 444,342 444,477 225,477" fill="var(--purple)"/>
      <rect x="444" y="0" width="225" height="477" fill="var(--paper)"/>
      <polygon points="444,0 669,0 669,12 444,52" fill="var(--teal)"/>
      <polygon points="444,180 669,155 669,162 444,188" fill="var(--purple)"/>
    </svg>
    <svg class="photo" style="left:225px;top:188px" width="219" height="174" role="img" aria-label="Photo of a business team meeting around a laptop">
      <defs><linearGradient id="g3" x1="0" y1="0" x2="1" y2="1"><stop offset="0" stop-color="#eef0f2"/><stop offset="1" stop-color="#7d848c"/></linearGradient></defs>
      <polygon points="0,51 219,7 219,148 0,174" fill="url(#g3)"/>
    </svg>
    <svg class="photo" style="left:444px;top:15px" width="225" height="165" role="img" aria-label="Photo of a group of smiling business professionals">
      <defs><linearGradient id="g4" x1="0" y1="0" x2="1" y2="1"><stop offset="0" stop-color="#e7eaed"/><stop offset="1" stop-color="#858b92"/></linearGradient></defs>
      <polygon points="0,40 225,0 225,140 0,165" fill="url(#g4)"/>
    </svg>

    <div class="tag" style="left:0;top:15px">ABOUT US</div>
    <div class="abs body-copy" style="left:12px;top:47px;width:200px">
      <p>Kelvora Staffing is a professional services organization offering human resources out-sourcing headquartered in Larkmont, CA.</p>
      <p style="margin-top:10px">If you have a business in California, you NEED HR expertise! Kelvora Staffing assists businesses who need HR assistance to remain compliant but simply do not have the need or budget for a full-time HR Manager.</p>
    </div>
    <div class="tag" style="left:0;top:165px">SERVICES PROVIDED</div>
    <ul class="abs checklist" style="left:12px;top:193px">
      <li>HR Compliance Audits</li>
      <li>Supervisor Training</li>
      <li>Part-Time HR</li>
      <li>Investigation Services</li>
      <li>I-9 Compliance</li>
      <li>Onboarding</li>
      <li>Terminations/RIFs</li>
      <li>Handbooks</li>
      <li>Compensation Analysis</li>
      <li>Performance Management</li>
      <li class="plain">Recruiting</li>
      <li class="plain">Employee Relations</li>
      <li class="plain">Benefits Admnistration</li>
      <li class="plain">Federal &amp; State Compliance</li>
    </ul>

    <div class="tag tag--light" style="left:225px;top:15px">OUR EXPERTISE</div>
    <ul class="abs checklist checklist--light" style="left:237px;top:38px">
      <li>Employee Relations</li>
      <li>Benefits Management</li>
      <li>Human Resources Compliance</li>
      <li>Training and Developmet</li>
      <li>Start Ups</li>
      <li>Strategic Planning</li>
      <li>Employee Handbooks</li>
      <li>OSHA Compliance</li>
      <li>Safety Training</li>
    </ul>
    <h2 class="abs pitch-title">HR Solutions</h2>
    <p class="abs pitch-sub">For The Business Owner</p>
    <div class="abs pitch-rule"></div>
    <p class="abs pitch-copy">We offer proven HR Consulting &amp; HR Outsourcing solutions to help businesses upgrade the bottom line on human resources and improve employee issues management.</p>

    <h2 class="abs experience-a">A More Complete</h2>
    <p class="abs experience-b">HR Experience</p>
    <p class="abs body-copy experience-copy">The need for Human Resources support can vary widely from organization to organization. Every company is unique from it's size to culture. To address this challenge, Kelvora Staffing can customize HR Solutions that work for your organizaion.</p>
    <div class="tag" style="left:444px;top:350px">OUR EXPERTISE</div>
    <ul class="abs benefits">
      <li><span class="dot"><svg width="10" height="8" viewBox="0 0 10 8"><circle cx="3" cy="2" r="1.6" fill="#fff"/><circle cx="7" cy="2" r="1.6" fill="#fff"/><rect x="0.5" y="4.5" width="9" height="3" rx="1.5" fill="#fff"/></svg></span>Risk Management</li>
      <li><span class="dot"><svg width="10" height="10" viewBox="0 0 10 10"><circle cx="5" cy="5" r="4" stroke="#fff" fill="none"/><text x="5" y="7.5" font-size="7" fill="#fff" text-anchor="middle" font-family="Arimo,sans-serif">$</text></svg></span>Cost Savings</li>
      <li><span class="dot"><svg width="10" height="9" viewBox="0 0 10 9"><rect x="1" y="5" width="2" height="4" fill="#fff"/><rect x="4" y="3" width="2" height="6" fill="#fff"/><rect x="7" y="1" width="2" height="8" fill="#fff"/></svg></span>Efficiency</li>
      <li><span class="dot"><svg width="6" height="10" viewBox="0 0 6 10"><circle cx="3" cy="2.5" r="2" stroke="#fff" fill="none"/><circle cx="3" cy="7" r="2.5" stroke="#fff" fill="none"/></svg></span>Build a Competitive Advantage</li>
    </ul>
  </section>

</div>
</body>
</html>
```